Birch Ledger brochure to showcase Masonry, landscape and concrete services

SEE RECENT COMMENT PAGE FOR BEST INFO We need a brochure designed to help inform our clients of our services and give them information on the pitfalls in the masonry, landscape and Hardscape industry, including drainage and frost protection, showcase some of our work we like to make all our material for marketing geared toward helping the client learn something. Drainage on any site is the number one component to a successful landscape, Hardscape and outdoor living area. This is often and overlooked to get to the stuff that's fun in turn, causing failure from frost due to northern Minnesota's harsh climate. Creating many disappointments on a large investment project. The brochure should also have a section focused on masonry, including fireplaces chimney repair, stucco repair, stone and brick. Some of the language should be editable. I will attach pictures and our logo.

Target Market(s)

Older customers with dual income looking to update and add outdoor living

Industry/Entity Type

Masonry, landscape, concrete, outdoor living

Font styles to use
Serif
Sans Serif
Other font styles liked:
• Arial

Colors

Designer to choose only greyscale colors for use in the design.

Requirements
Must have
• I really like gray, silver and black when I do marketing mixed with White, but I thought adding some greenery for the landscape portion might look good too on this brochure
Nice to have
• I do not like it too busy so keep it clean and simple
Should not have
• Tons of clutter, tons of words, hard to read and look at

```html
<!DOCTYPE html>
<html lang="en">
<head>
<meta charset="utf-8">
<title>Birch Ledger – Masonry, Landscape &amp; Outdoor Living</title>
<link href="https://fonts.googleapis.com/css2?family=Archivo+Black&family=Arimo:wght@400;700&display=swap" rel="stylesheet">
<style>
  :root {
    --ink: #2b2b2d;
    --ink-soft: #3a3a3c;
    --panel-top: #333336;
    --panel-bottom: #222224;
    --silver: #b9b9bb;
    --silver-light: #d2d2d4;
    --rule: #9a9a9c;
    --white: #ffffff;
    --mint: #dcefe2;
    --sky: #5c85c6;
    --mark-grey: #77787a;
  }
  * { margin: 0; padding: 0; box-sizing: border-box; }
  html, body { width: 1200px; height: 843px; overflow: hidden; background: var(--white); }
  body { font-family: "Arimo", Arial, sans-serif; color: var(--ink); }
  .brochure { position: relative; width: 1200px; height: 843px; overflow: hidden; background: var(--white); }
  .layer { position: absolute; inset: 0; }

  .headline {
    font-family: "Archivo Black", "Arial Black", sans-serif;
    font-size: 31px; line-height: 38px; color: var(--ink); position: absolute;
  }
  .headline .muted {
    background: linear-gradient(90deg, #8c8c8e, var(--silver-light));
    -webkit-background-clip: text; background-clip: text; color: transparent;
  }
  .accent-bar { position: absolute; width: 55px; height: 3px; border-radius: 2px;
    background: linear-gradient(90deg, var(--rule), var(--silver-light)); }
  .body-copy { position: absolute; font-size: 12.3px; line-height: 20px; color: var(--ink-soft); }
  .subhead { position: absolute; font-size: 14.5px; font-weight: 700; color: var(--ink); }

  /* drainage column */
  .focus-list { position: absolute; left: 36px; top: 313px; width: 327px; list-style: none; }
  .focus-list li { position: relative; height: 51px; display: flex; align-items: center;
    padding-left: 36px; font-size: 12.3px; color: var(--ink-soft); }
  .focus-list li + li::before { content: ""; position: absolute; left: 36px; right: 0; top: 0;
    border-top: 1px solid #c7c7c9; }
  .focus-list svg { position: absolute; left: 0; top: 12px; width: 28px; height: 28px; }

  /* masonry panel */
  .masonry-panel { position: absolute; left: 437px; top: 34px; width: 325px; height: 820px;
    border-radius: 9px 9px 0 0;
    background: linear-gradient(180deg, var(--panel-top), var(--panel-bottom)); }
  .masonry-panel .headline { color: var(--white); left: 40px; top: 26px; }
  .masonry-panel .body-copy { color: var(--white); }
  .service-list { position: absolute; left: 38px; top: 236px; width: 253px; list-style: none; }
  .service-list li { position: relative; height: 42.5px; display: flex; align-items: center;
    padding-left: 38px; font-size: 15px; font-weight: 700; color: var(--white); }
  .service-list li + li::before { content: ""; position: absolute; left: 38px; right: 0; top: 0;
    border-top: 1px solid #5c5c5f; }
  .service-list svg { position: absolute; left: 0; top: 8px; width: 28px; height: 28px; }

  .brand-badge { position: absolute; left: 503px; top: 534px; width: 194px; height: 194px;
    border-radius: 50%; background: var(--mark-grey);
    display: flex; align-items: center; justify-content: center; }
  .brand-name { font-family: "Archivo Black", "Arial Black", sans-serif; font-size: 22px;
    color: var(--panel-bottom); }

  /* outdoor spaces column */
  .build-list { position: absolute; left: 836px; top: 637px; width: 326px; list-style: none; }
  .build-list li { position: relative; height: 31px; display: flex; align-items: center;
    padding-left: 20px; font-size: 12.3px; color: var(--ink-soft); }
  .build-list li + li::before { content: ""; position: absolute; left: 0; right: 0; top: 0;
    border-top: 1px solid #8e8e90; }
  .build-list svg { position: absolute; left: 0; top: 9px; width: 13px; height: 13px; }
</style>
</head>
<body>
<main class="brochure">

  <!-- background shapes and photo areas -->
  <svg class="layer" width="1200" height="843" viewBox="0 0 1200 843">
    <defs>
      <linearGradient id="house-photo" x1="0" y1="0" x2="0" y2="1">
        <stop offset="0" stop-color="#6f93c9"/>
        <stop offset="0.45" stop-color="#556a8d"/>
        <stop offset="0.7" stop-color="#a58463"/>
        <stop offset="1" stop-color="#7d6676"/>
      </linearGradient>
      <linearGradient id="fireplace-photo" x1="0" y1="0" x2="0" y2="1">
        <stop offset="0" stop-color="#b48a55"/>
        <stop offset="0.4" stop-color="#9d958c"/>
        <stop offset="1" stop-color="#5a5550"/>
      </linearGradient>
      <linearGradient id="ground" x1="0" y1="0" x2="0" y2="1">
        <stop offset="0" stop-color="#3a3a3d"/>
        <stop offset="1" stop-color="#6a6a6d"/>
      </linearGradient>
    </defs>
    <circle cx="1000" cy="-150" r="500" fill="var(--sky)"/>
    <circle cx="1260" cy="200" r="310" fill="var(--mint)"/>
    <circle cx="155" cy="800" r="310" fill="var(--mint)"/>
  </svg>

  <div class="masonry-panel">
    <h2 class="headline">Masonry<br><span class="muted">Expertise</span> You<br>Can Trust</h2>
    <div class="accent-bar" style="left:41px; top:152px;"></div>
    <p class="body-copy" style="left:41px; top:176px; width:250px;">Our masonry services combine artistry with durability, including:</p>
    <ul class="service-list">
      <li>
        <svg viewBox="0 0 28 28" fill="none" stroke="#cfcfd1" stroke-width="1.2"><rect x="6" y="10" width="16" height="16"/><path d="M6 14h16M6 18h16M6 22h16M11 10v4M17 10v4M9 14v4M14 14v4M19 14v4M11 18v4M17 18v4M9 22v4M14 22v4M19 22v4M12 8c-1-2 1-3 0-5M16 8c-1-2 1-3 0-5"/></svg>
        Fireplaces &amp; chimneys
      </li>
      <li>
        <svg viewBox="0 0 28 28" fill="none" stroke="#cfcfd1" stroke-width="1.2"><rect x="2" y="2" width="24" height="24"/><path d="M2 8h24M2 14h8M8 2v6M16 2v6M22 8v6M2 19l6-4 6 6 6-3 6 4"/></svg>
        Stucco repair &amp; restoration
      </li>
      <li>
        <svg viewBox="0 0 28 28" fill="none" stroke="#cfcfd1" stroke-width="1.2"><rect x="2" y="4" width="22" height="22"/><path d="M2 9h22M2 14h22M2 19h22M8 4v5M15 4v5M5 9v5M12 9v5M19 9v5M8 14v5M15 14v5M5 19v7M12 19v7M22 14l4 8-4 4"/></svg>
        Stone &amp; brick walls
      </li>
      <li>
        <svg viewBox="0 0 28 28" fill="none" stroke="#cfcfd1" stroke-width="1.2"><path d="M14 2v4M9 6h10l2 5H7zM5 11h18v4H5zM8 15v10M20 15v10M8 20h12M4 25h20"/></svg>
        Custom &amp; outdoor kitchens
      </li>
    </ul>
    <p class="body-copy" style="left:41px; top:429px; width:255px;">Every project is crafted to last, adding beauty and functionality to your home.</p>
  </div>

  <div class="brand-badge"><span class="brand-name">Birch Ledger</span></div>

  <svg class="layer" width="1200" height="843" viewBox="0 0 1200 843">
    <path d="M330 650 C 460 610, 640 640, 780 860 L 330 860 Z" fill="url(#ground)" stroke="var(--white)" stroke-width="9"/>
    <rect x="762" y="0" width="438" height="440" fill="none"/>
    <path d="M762 0 H1200 V380 A548 548 0 0 1 762 418 Z" fill="url(#house-photo)" role="img" aria-label="Photo of a blue house with a new screened porch and insulated concrete forms laid for a patio slab"/>
    <circle cx="105" cy="790" r="282" fill="url(#fireplace-photo)" role="img" aria-label="Photo of a river-stone fireplace with a log mantel in a cedar-walled cabin"/>
  </svg>

  <h1 class="headline" style="left:36px; top:28px;">The Secret to a<br><span class="muted">Successful</span> Outdoor<br>Project</h1>
  <div class="accent-bar" style="left:36px; top:155px;"></div>
  <p class="body-copy" style="left:36px; top:176px; width:335px;">Proper drainage is the #1 component for a durable landscape and hardscape. Overlooking this step can lead to frost damage, soil erosion, and project failures—turning your dream outdoor space into a costly disappointment.</p>
  <h3 class="subhead" style="left:36px; top:282px;">We focus on:</h3>
  <ul class="focus-list">
    <li>
      <svg viewBox="0 0 28 28" fill="none" stroke="#4a4a4c" stroke-width="1.2"><path d="M14 2L2 25h24zM14 8L7 21h14zM5 20l6-5 4 3 5-4"/></svg>
      Site grading &amp; slope management
    </li>
    <li>
      <svg viewBox="0 0 28 28" fill="none" stroke="#4a4a4c" stroke-width="1.2"><path d="M2 14h24M4 16h4v10H4zM10 16h4v10h-4zM16 16h4v10h-4zM22 16h4v10h-4zM8 10c0-3 3-4 3-7 0 3 3 4 3 7a3 3 0 0 1-6 0zM16 10c0-2 2-3 2-5 0 2 2 3 2 5a2 2 0 0 1-4 0z"/></svg>
      Drainage solutions for every landscape type
    </li>
    <li>
      <svg viewBox="0 0 28 28" fill="none" stroke="#4a4a4c" stroke-width="1.2"><path d="M13 2l10 4v7c0 7-5 11-10 13C8 24 3 20 3 13V6z"/><circle cx="19" cy="19" r="7" fill="#fff"/><path d="M19 13v12M13 19h12M15 15l8 8M23 15l-8 8"/></svg>
      Frost protection to prevent winter damage
    </li>
  </ul>

  <h2 class="headline" style="left:836px; top:497px;">Creating Outdoor<br><span class="muted">Spaces</span> You’ll Love</h2>
  <div class="accent-bar" style="left:837px; top:588px;"></div>
  <h3 class="subhead" style="left:836px; top:606px;">We design and build:</h3>
  <ul class="build-list">
    <li><svg viewBox="0 0 13 13"><circle cx="6.5" cy="6.5" r="6.5" fill="var(--ink)"/><path d="M3.5 6.7l2 2 4-4.2" fill="none" stroke="#fff" stroke-width="1.5"/></svg>Patios, walkways, and driveways</li>
    <li><svg viewBox="0 0 13 13"><circle cx="6.5" cy="6.5" r="6.5" fill="var(--ink)"/><path d="M3.5 6.7l2 2 4-4.2" fill="none" stroke="#fff" stroke-width="1.5"/></svg>Retaining walls and terraces</li>
    <li><svg viewBox="0 0 13 13"><circle cx="6.5" cy="6.5" r="6.5" fill="var(--ink)"/><path d="M3.5 6.7l2 2 4-4.2" fill="none" stroke="#fff" stroke-width="1.5"/></svg>Outdoor kitchens &amp; living areas</li>
    <li><svg viewBox="0 0 13 13"><circle cx="6.5" cy="6.5" r="6.5" fill="var(--ink)"/><path d="M3.5 6.7l2 2 4-4.2" fill="none" stroke="#fff" stroke-width="1.5"/></svg>Gardens and green spaces</li>
  </ul>
  <p class="body-copy" style="left:838px; top:772px; width:330px;">We prioritize smart planning and solid construction so your investment lasts for years to come.</p>

</main>
</body>
</html>
```